Brightwave Reach - Business Card

We need a business card for a Social Media Marketing company that specializes in online marketing for small businesses in Canada using common Social Media platforms such as Pictora, Kinloop, Glimmo & Chirpo.

I have uploaded a copy of our logo which I would like utilized in the business card. We would like the business card to be modern yet classy design.

Our website is www.brightwavereach.ca

Industry/Entity Type

Marketing

Contact Information for Business Card

Email: info@brightwavereach.ca
Website: www.brightwavereach.ca
Telephone: 604-392-5108

Colors

Designer to choose colors to be used in the design.

Requirements
Must have
• Social Media icons on reverse
• Please add some designs with color.

```html
<!DOCTYPE html>
<html lang="en">
<head>
<meta charset="utf-8">
<title>Brightwave Reach – Business Card</title>
<link rel="stylesheet" href="https://fonts.googleapis.com/css2?family=Roboto+Condensed:wght@400;700&display=swap">
<style>
  :root {
    --backdrop: #1f2021;
    --card-white: #f4f4f3;
    --slate: #4a5153;
    --slate-dark: #3f4547;
    --ink: #3a3f41;
  }
  * { box-sizing: border-box; margin: 0; padding: 0; }
  html, body { width: 1200px; height: 1000px; overflow: hidden; }
  body {
    background: var(--backdrop);
    font-family: "Roboto Condensed", "Arial Narrow", sans-serif;
    position: relative;
  }
  .card {
    position: absolute;
    width: 490px;
    height: 280px;
    top: 360px;
    overflow: hidden;
    box-shadow: 0 10px 24px rgba(0,0,0,.45);
  }
  .card--front { left: 85px; background: var(--card-white); }
  .card--back { left: 625px; background: var(--slate); }

  /* brand mark stand-in */
  .brand {
    position: absolute;
    display: flex;
    align-items: center;
    gap: 8px;
    color: var(--ink);
    font-weight: 700;
    text-transform: uppercase;
    line-height: 1;
    white-space: nowrap;
  }
  .brand__square {
    width: 13px; height: 13px;
    background: currentColor;
    flex: none;
  }
  .card--front .brand { left: 28px; top: 36px; font-size: 22px; }
  .card--back .brand {
    left: 50%; top: 82px; transform: translateX(-40%);
    font-size: 24px; color: var(--card-white);
  }

  /* front details */
  .front__rule {
    position: absolute;
    left: 265px; right: 0; top: 112px;
    height: 9px; background: var(--slate);
  }
  .front__stripe {
    position: absolute; left: 0; width: 215px;
    top: 178px; height: 8px; background: var(--slate);
  }
  .front__band {
    position: absolute; left: 0; width: 205px;
    top: 198px; bottom: 0; background: var(--slate);
  }
  .contact {
    position: absolute; left: 240px; top: 140px;
    color: var(--ink);
  }
  .contact__name { font-size: 17px; font-weight: 700; text-transform: uppercase; letter-spacing: .3px; line-height: 20px; }
  .contact__role { font-size: 13px; line-height: 16px; margin-bottom: 8px; }
  .contact__row { display: flex; align-items: center; gap: 7px; font-size: 13px; line-height: 18px; white-space: nowrap; }
  .contact__row svg { width: 11px; height: 11px; fill: var(--ink); flex: none; }

  /* back details */
  .back__art { position: absolute; inset: 0; }
  .social__label {
    font-family: "Roboto Condensed", "Arial Narrow", sans-serif;
    font-size: 8.5px; font-weight: 700; fill: var(--card-white);
  }
</style>
</head>
<body>

<section class="card card--front" aria-label="Card front">
  <div class="brand"><span class="brand__square"></span>Brightwave Reach</div>
  <div class="front__rule"></div>
  <div class="front__stripe"></div>
  <div class="front__band"></div>
  <div class="contact">
    <p class="contact__name">Daniel Hartley</p>
    <p class="contact__role">Manager</p>
    <p class="contact__row">
      <svg viewBox="0 0 12 12"><path d="M2.5 0.5 4.5 3 3.5 4.5c.8 1.6 2 2.8 3.9 3.9L8.9 7.5 11.5 9.5 10.2 11.5C5.5 11 1 6.5.5 1.8Z"/></svg>
      604-392-5108
    </p>
    <p class="contact__row">
      <svg viewBox="0 0 12 12"><path d="M0 2h12v8H0Zm1 1 5 3.5L11 3Z" fill-rule="evenodd"/></svg>
      info@brightwavereach.ca
    </p>
    <p class="contact__row">
      <svg viewBox="0 0 12 12"><circle cx="6" cy="6" r="5.5"/><path d="M.5 6h11M6 .5v11" stroke="#f4f4f3" stroke-width="1"/></svg>
      www.brightwavereach.ca
    </p>
  </div>
</section>

<section class="card card--back" aria-label="Card back">
  <svg class="back__art" viewBox="0 0 490 280" width="490" height="280">
    <path d="M0 208 H50 L60 198 H88 L98 208 L400 262 L410 252 H440 L450 262 H490 V280 H0 Z" fill="var(--card-white)"/>
    <g>
      <circle cx="135" cy="221" r="18" fill="var(--slate-dark)"/>
      <text class="social__label" x="135" y="224" text-anchor="middle">Chirpo</text>
      <circle cx="205" cy="234" r="18" fill="var(--slate-dark)"/>
      <text class="social__label" x="205" y="237" text-anchor="middle">Glimmo</text>
      <circle cx="275" cy="246" r="18" fill="var(--slate-dark)"/>
      <text class="social__label" x="275" y="249" text-anchor="middle">Pictora</text>
      <circle cx="345" cy="258" r="18" fill="var(--slate-dark)"/>
      <text class="social__label" x="345" y="261" text-anchor="middle">Kinloop</text>
    </g>
  </svg>
  <div class="brand"><span class="brand__square"></span>Brightwave Reach</div>
</section>

</body>
</html>
```